Simple AD for Digital Publication

Total Size 5" x 5", may include boarder or not
Image Provided; crop or use as background
Incorporate Logo and text as provided

Target Market(s)

Sound Contractors / Integrators

Industry/Entity Type

Audio Video Lighting

Requirements
Must have
• Bold Look that reflects our brand. see website: tovermundic.com - cohesive text and style

```html
<!DOCTYPE html>
<html lang="en">
<head>
<meta charset="UTF-8">
<title>Tovermund – Become a Dealer</title>
<link href="https://fonts.googleapis.com/css2?family=Montserrat:wght@600;700;800&display=swap" rel="stylesheet">
<style>
  :root {
    --brand-red: #c20a0a;
    --ink-dark: #3b3b3d;
    --white: #ffffff;
    --scene-top: #3a3633;
    --scene-mid: #4a5146;
    --scene-low: #6b625a;
    --scene-floor: #8a8078;
    --veil: rgba(40, 36, 34, 0.55);
  }
  * { margin: 0; padding: 0; box-sizing: border-box; }
  html, body { width: 1200px; height: 1200px; overflow: hidden; background: #2e2b29; }
  body { font-family: "Montserrat", Arial, sans-serif; }

  .ad {
    position: relative;
    width: 1200px;
    height: 1200px;
    overflow: hidden;
  }

  .ad__scene {
    position: absolute;
    inset: 0;
    background:
      radial-gradient(ellipse 60% 22% at 45% 42%, rgba(120, 135, 100, 0.55), transparent 70%),
      radial-gradient(ellipse 30% 14% at 62% 68%, rgba(30, 30, 32, 0.55), transparent 75%),
      linear-gradient(180deg, var(--scene-top) 0%, var(--scene-mid) 38%, var(--scene-low) 62%, var(--scene-floor) 100%);
  }
  .ad__veil { position: absolute; inset: 0; background: var(--veil); }

  .ad__shapes { position: absolute; inset: 0; }

  .brand {
    position: absolute;
    top: 46px;
    left: 0;
    width: 1200px;
    text-align: center;
  }
  .brand__name {
    display: block;
    font-weight: 800;
    font-size: 44px;
    line-height: 50px;
    color: var(--ink-dark);
    letter-spacing: 2px;
  }
  .brand__tagline {
    display: block;
    margin-top: 4px;
    font-weight: 600;
    font-size: 20px;
    line-height: 26px;
    color: var(--ink-dark);
  }

  .headline {
    position: absolute;
    top: 500px;
    left: 0;
    width: 1200px;
    text-align: center;
    color: var(--white);
    font-weight: 700;
    font-size: 76px;
    line-height: 92px;
    text-shadow: 0 2px 8px rgba(0, 0, 0, 0.35);
  }

  .cta {
    position: absolute;
    top: 988px;
    left: 0;
    width: 1200px;
    display: flex;
    flex-direction: column;
    align-items: center;
  }
  .cta__lead {
    color: var(--white);
    font-weight: 700;
    font-size: 38px;
    line-height: 50px;
  }
  .cta__button {
    margin-top: 10px;
    width: 578px;
    height: 82px;
    border-radius: 41px;
    background: var(--brand-red);
    color: var(--white);
    font-weight: 700;
    font-size: 47px;
    letter-spacing: 3px;
    display: flex;
    align-items: center;
    justify-content: center;
    text-decoration: none;
  }
</style>
</head>
<body>
  <main class="ad">
    <div class="ad__scene" role="img" aria-label="Photo of a wooden stage floor with an open floor pocket box and cables, a lit evergreen garland and chairs behind"></div>
    <div class="ad__veil"></div>

    <svg class="ad__shapes" width="1200" height="1200" viewBox="0 0 1200 1200" aria-hidden="true">
      <polygon points="120,0 1080,0 600,330" fill="rgba(255,255,255,0.14)"/>
      <path d="M194,0 H1006 L628,258 Q600,276 572,258 Z" fill="#ffffff"/>
      <polygon points="0,720 150,900 0,1080" fill="rgba(255,255,255,0.08)"/>
      <polygon points="1200,720 1050,900 1200,1080" fill="rgba(255,255,255,0.08)"/>
    </svg>

    <header class="brand">
      <span class="brand__name">TOVERMUND</span>
      <span class="brand__tagline">Stage Pocket Systems Connectivity</span>
    </header>

    <h1 class="headline">Protect and Conceal<br>High and Low Voltage<br>Connectivity</h1>

    <section class="cta">
      <p class="cta__lead">Become a Dealer</p>
      <a class="cta__button" href="#">CLICK HERE</a>
    </section>
  </main>
</body>
</html>
```